New modern website for Kerbline Groundworks

Hi we are an existing company that has a current website http://www.kerblinegroundworks.co.nz/ we are looking to get a new vibrant looking website designed to take us further and gain more customers. We are after a simple easy to use website that does not confuse but we want to make an impact and stand out from the rest

Target Market(s)

Homeowners And Commercial Businesses

Industry/Entity Type

It Company

Coding

Coded - Design and coding required

Number of Pages Required

2 page

```html
<!DOCTYPE html>
<html lang="en">
<head>
<meta charset="utf-8">
<title>Kerbline Groundworks</title>
<link rel="stylesheet" href="https://fonts.googleapis.com/css2?family=Roboto:wght@300;400;500;700&family=Raleway:wght@400;500;600;700&display=swap">
<style>
:root{
  --yellow:#f5b21b;
  --yellow-bright:#fdd017;
  --ink:#141414;
  --line:#3a3a3a;
  --text:#e8e8e8;
  --footer:#0a0a0a;
  --social:#2a7bd1;
  --icon-grey:#3a3a3a;
}
*{box-sizing:border-box;margin:0;padding:0}
html,body{width:1200px;height:2616px;overflow:hidden;background:var(--ink)}
body{position:relative;font-family:"Roboto",Arial,sans-serif;color:var(--text)}
.abs{position:absolute}

/* hero */
.hero-photo{left:0;top:0;width:1200px;height:628px;background:linear-gradient(100deg,#7d8079 0%,#5e5f59 35%,#8a7d3e 62%,#4a4a44 80%,#2c2c2a 100%)}
.site-header{left:0;top:0;width:1200px;height:94px;background:rgba(10,10,10,.72)}
.brand{left:99px;top:26px;display:flex;align-items:center;gap:12px;font-family:"Raleway",sans-serif;font-weight:700;font-size:24px;color:#fff;letter-spacing:.5px}
.brand-dot{width:16px;height:16px;border-radius:50%;background:#fff}
.phone-tag{left:853px;top:12px;width:103px;height:28px;background:#3c3c3c;color:#fff;font-size:14px;font-weight:500;line-height:28px;text-align:center}
.quote-tag{left:956px;top:12px;width:146px;height:28px}
.quote-tag span{position:absolute;left:24px;top:0;line-height:28px;font-size:12px;font-weight:500;color:#111}
.main-nav{left:640px;top:52px;display:flex;font-family:"Raleway",sans-serif;font-weight:600;font-size:13px;color:#fff}
.main-nav a{color:#fff;text-decoration:none;padding:6px 12px;margin-right:22px;border:2px solid transparent}
.main-nav a.active{border-color:var(--yellow-bright);color:var(--yellow-bright)}
.main-nav a:last-child{margin-right:0}
.hero-title{left:99px;top:258px;font-size:42px;line-height:46px;font-weight:400;color:#fff}
.hero-title strong{display:block;color:var(--yellow-bright);font-weight:500}

.quote-form{left:759px;top:140px;width:402px;height:441px;background:rgba(8,8,8,.92)}
.quote-banner{left:0;top:0;width:402px;height:96px}
.quote-banner h2{position:absolute;left:0;top:14px;width:402px;text-align:center;font-family:"Raleway",sans-serif;font-size:23px;font-weight:700;color:#111}
.quote-banner p{position:absolute;left:0;top:46px;width:402px;text-align:center;font-family:"Raleway",sans-serif;font-size:16px;font-weight:600;color:#111}
.field{left:26px;width:352px;height:42px;border:1px solid #555;background:#101010;color:#aaa;font-family:"Raleway",sans-serif;font-size:17px;line-height:40px;padding-left:12px}
.field svg{position:absolute;right:14px;top:14px}
.submit{left:26px;top:366px;width:352px;height:49px;background:var(--yellow);color:#111;font-family:"Raleway",sans-serif;font-weight:700;font-size:22px;text-align:center;line-height:49px}

.dash{height:6px;background:repeating-linear-gradient(90deg,var(--yellow-bright) 0 14px,transparent 14px 24px)}
.stripe{background:var(--yellow)}

/* intro */
.intro-title{left:0;top:688px;width:1200px;text-align:center;font-size:31px;font-weight:300;color:#fff;line-height:44px}
.intro-title strong{display:block;font-weight:500}
.feature{width:330px;text-align:center}
.feature-icon{height:150px;display:flex;align-items:center;justify-content:center}
.icon-disc{width:154px;height:154px;border-radius:50%;background:var(--icon-grey);border:4px solid #222}
.icon-tile{width:110px;height:110px;border-radius:8px;background:linear-gradient(180deg,#3d3d3d 0%,#3d3d3d 70%,#8a6d16 100%)}
.feature h3{margin-top:22px;font-size:16px;font-weight:500;color:#fff}
.feature p{margin:12px auto 0;width:260px;font-size:11.5px;line-height:15.5px;color:#bdbdbd}
.divider{width:1px;height:279px;background:var(--line)}

/* cards */
.card{width:487px;height:257px;overflow:hidden}
.card-photo{position:absolute;inset:0}
.card-shade{position:absolute;inset:0;background:linear-gradient(180deg,rgba(0,0,0,0) 45%,rgba(0,0,0,.85) 100%)}
.card h3{position:absolute;left:25px;top:148px;font-size:34px;font-weight:400;color:#fff;padding-bottom:4px;border-bottom:4px solid var(--yellow-bright)}
.card p{position:absolute;left:25px;top:214px;font-size:16px;color:#fff}

.section-head{left:99px;width:1002px;text-align:center}
.section-head h2{display:inline-block;background:var(--ink);padding:0 24px;position:relative;font-size:25px;font-weight:400;color:#fff}
.section-head::before{content:"";position:absolute;left:30px;right:30px;top:50%;height:1px;background:var(--line)}
.section-sub{left:0;width:1200px;text-align:center;font-size:14px;color:#b5b5b5}

/* testimonials */
.testimonial{width:317px;height:166px;border:1.5px solid #6f5a1e;padding:22px 24px 0 36px}
.testimonial p{font-size:13px;line-height:20px;color:#8c8c8c;margin-bottom:20px}
.open-mark{position:absolute;left:10px;top:12px;font-family:Georgia,serif;font-size:40px;color:#7a6a40;line-height:1}
.close-mark{font-family:Georgia,serif;font-size:30px;color:#7a6a40;line-height:0;vertical-align:-10px;margin-left:4px}
.tail{position:absolute;right:-2px;bottom:-24px}
.author{display:flex;align-items:center;gap:10px}
.avatar{width:40px;height:40px;border-radius:50%;background:linear-gradient(#b8a89a,#6d5e57)}
.author b{display:block;font-size:13px;font-weight:700;color:#d6d6d6}
.author small{display:block;font-size:10.5px;color:#9a9a9a}

.gallery-item{top:2084px;width:231px;height:143px}

/* cta */
.cta{left:99px;top:2288px;width:1003px;height:136px;background:#050505;overflow:hidden}
.cta-ask{left:34px;top:32px;font-size:24px;font-weight:400;color:#fff}
.cta-talk{left:34px;top:64px;font-size:39px;font-weight:700;color:var(--yellow-bright)}
.cta-numbers{left:560px;top:16px;font-size:40px;font-weight:700;line-height:52px;color:#111;white-space:nowrap}

/* footer */
.site-footer{left:0;top:2529px;width:1200px;height:87px;background:var(--footer)}
.footer-nav{left:99px;top:24px;display:flex;gap:31px;font-size:12px;color:#9a9a9a}
.copyright{left:99px;top:48px;font-size:10px;color:#555}
.social{top:20px;width:46px;height:46px;border:2px solid var(--social);border-radius:50%}
</style>
</head>
<body>

<div class="abs hero-photo" role="img" aria-label="Asphalt paving truck spreading hot gravel on a road with steam rising"></div>

<header class="abs site-header">
  <div class="abs brand"><span class="brand-dot"></span>Kerbline Groundworks</div>
  <div class="abs phone-tag">09 555 0142</div>
  <div class="abs quote-tag">
    <svg width="146" height="28" viewBox="0 0 146 28"><polygon points="0,0 146,0 136,14 146,28 0,28" fill="#fdd017"/></svg>
    <span>REQUEST QUOTE</span>
  </div>
  <nav class="abs main-nav">
    <a class="active">HOME</a><a>ABOUT</a><a>SERVICES</a><a>PROJECTS</a><a>CONTACT US</a>
  </nav>
</header>

<h1 class="abs hero-title">Setting the standards for<strong>Concrete and Asphalters</strong></h1>

<form class="abs quote-form">
  <div class="abs quote-banner">
    <svg width="402" height="96" viewBox="0 0 402 96"><polygon points="0,0 402,0 402,70 201,96 0,70" fill="#f5b21b"/></svg>
    <h2>GET INSTANT ONLINE QUOTE</h2>
    <p>START HERE NOW</p>
  </div>
  <div class="abs field" style="top:127px">Name</div>
  <div class="abs field" style="top:186px">Mobile Number</div>
  <div class="abs field" style="top:245px">Email Adress</div>
  <div class="abs field" style="top:305px">Solutions Requested
    <svg width="18" height="12" viewBox="0 0 18 12"><polyline points="1,2 9,10 17,2" fill="none" stroke="#ddd" stroke-width="2"/></svg>
  </div>
  <div class="abs submit">SUBMIT NOW!</div>
</form>

<div class="abs dash" style="left:0;top:626px;width:1200px"></div>

<!-- intro -->
<div class="abs stripe" style="left:0;top:659px;width:40px;height:361px"></div>
<div class="abs stripe" style="left:61px;top:659px;width:40px;height:361px"></div>
<div class="abs stripe" style="left:1097px;top:814px;width:42px;height:363px"></div>
<div class="abs stripe" style="left:1160px;top:814px;width:40px;height:363px"></div>

<h2 class="abs intro-title">The trusted name for all<strong>Concrete &amp; Asphalt Paving in Auckland</strong></h2>

<div class="abs feature" style="left:97px;top:830px">
  <div class="feature-icon"><span class="icon-disc" role="img" aria-label="Experience badge"></span></div>
  <h3>Years of Experience</h3>
  <p>We have a reputation with clients in and around Auckland for achieving great results on time and within budget every time. We are proud to share our years of experience.</p>
</div>
<div class="abs divider" style="left:427px;top:820px"></div>
<div class="abs feature" style="left:435px;top:830px">
  <div class="feature-icon"><span class="icon-tile" role="img" aria-label="Illustration of a home with a paved driveway"></span></div>
  <h3>Concreting &amp; Asphalt Work</h3>
  <p>When it comes to all asphalt services, you can rest assured we will work around your schedule, requirements and budget. Servicing throughout Auckland, we specialise in.</p>
</div>
<div class="abs divider" style="left:760px;top:820px"></div>
<div class="abs feature" style="left:758px;top:830px">
  <div class="feature-icon"><span class="icon-tile" role="img" aria-label="Illustration of a sealed road"></span></div>
  <h3>Additional Services</h3>
  <p>As part of our asphalt services, we are proud to offer a range of related services to our clients in the eastern suburbs and greater Auckland. Specialising in residential, commercial and industrial projects.</p>
</div>

<div class="abs dash" style="left:0;top:1172px;width:1200px"></div>

<!-- diagonal bands -->
<svg class="abs" style="left:0;top:1420px" width="1200" height="640" viewBox="0 0 1200 640">
  <polygon points="1100,45 1128,45 1200,140 1200,180" fill="#f5b21b"/>
  <polygon points="1040,80 1080,80 1200,240 1200,300" fill="#f5b21b"/>
  <polygon points="0,358 0,418 96,540 96,480" fill="#f5b21b"/>
  <polygon points="0,440 0,500 96,620 96,560" fill="#f5b21b"/>
</svg>

<!-- cards -->
<div class="abs card" style="left:99px;top:1238px">
  <div class="card-photo" role="img" aria-label="Paving crew in hi-vis working beside a dump truck and asphalt paver" style="background:linear-gradient(160deg,#bcc6cf 0%,#8c8a78 40%,#6a6a52 70%,#3a3a30 100%)"></div>
  <div class="card-shade"></div>
  <h3>Services</h3>
  <p>Complete asphalt services for your next</p>
</div>
<div class="abs card" style="left:612px;top:1238px">
  <div class="card-photo" role="img" aria-label="Freshly sealed residential driveway lined with garden plants" style="background:linear-gradient(160deg,#d8dccf 0%,#7e8a5c 35%,#4e5c38 60%,#2e2e2c 100%)"></div>
  <div class="card-shade"></div>
  <h3>Projects</h3>
  <p>For residential driveways and commercial</p>
</div>

<div class="abs dash" style="left:99px;top:1550px;width:947px"></div>

<!-- testimonials -->
<div class="abs section-head" style="top:1609px"><h2>Customer Testimonials</h2></div>

<div class="abs testimonial" style="left:99px;top:1669px">
  <span class="open-mark">&ldquo;</span>
  <p>Lorem ipsum dolor sit amet, consectetur adipiscing elit, sed do eiusmod tempor incididunt ut labore et dolore magna aliqua.</p>
  <p>Sed ut perspiciatis unde omnis iste natus error sit voluptatem accusantium<span class="close-mark">&rdquo;</span></p>
  <svg class="tail" width="26" height="26" viewBox="0 0 26 26"><polygon points="0,0 24,0 24,24" fill="#141414" stroke="#6f5a1e" stroke-width="1.5"/></svg>
</div>
<div class="abs author" style="left:250px;top:1855px"><span class="avatar" role="img" aria-label="Client portrait"></span><span><b>John Smith</b><small>CEO, Abc Company</small></span></div>

<div class="abs testimonial" style="left:441px;top:1669px">
  <span class="open-mark">&ldquo;</span>
  <p>Lorem ipsum dolor sit amet, consectetur adipiscing elit, sed do eiusmod tempor incididunt ut labore et dolore magna aliqua.</p>
  <p>Sed ut perspiciatis unde omnis iste natus error sit voluptatem accusantium<span class="close-mark">&rdquo;</span></p>
  <svg class="tail" width="26" height="26" viewBox="0 0 26 26"><polygon points="0,0 24,0 24,24" fill="#141414" stroke="#6f5a1e" stroke-width="1.5"/></svg>
</div>
<div class="abs author" style="left:594px;top:1855px"><span class="avatar" role="img" aria-label="Client portrait"></span><span><b>John Smith</b><small>CEO, Abc Company</small></span></div>

<div class="abs testimonial" style="left:783px;top:1669px">
  <span class="open-mark">&ldquo;</span>
  <p>Lorem ipsum dolor sit amet, consectetur adipiscing elit, sed do eiusmod tempor incididunt ut labore et dolore magna aliqua.</p>
  <p>Sed ut perspiciatis unde omnis iste natus error sit voluptatem accusantium<span class="close-mark">&rdquo;</span></p>
  <svg class="tail" width="26" height="26" viewBox="0 0 26 26"><polygon points="0,0 24,0 24,24" fill="#141414" stroke="#6f5a1e" stroke-width="1.5"/></svg>
</div>
<div class="abs author" style="left:936px;top:1855px"><span class="avatar" role="img" aria-label="Client portrait"></span><span><b>John Smith</b><small>CEO, Abc Company</small></span></div>

<!-- gallery -->
<div class="abs section-head" style="top:1986px"><h2>Our Project Gallery</h2></div>
<div class="abs section-sub" style="top:2030px">For residential driveways and commercial paving in Auckland</div>

<div class="abs gallery-item" style="left:99px;background:linear-gradient(180deg,#c9cfd3 0%,#a8aaa6 45%,#8d8f8c 100%)" role="img" aria-label="Workers finishing a wet concrete slab"></div>
<div class="abs gallery-item" style="left:356px;background:linear-gradient(180deg,#9fa6ad 0%,#7c7a70 40%,#b9bab6 100%)" role="img" aria-label="Large commercial yard after asphalt sealing"></div>
<div class="abs gallery-item" style="left:614px;background:linear-gradient(180deg,#3f5a2e 0%,#5a6b40 40%,#4b4b48 100%)" role="img" aria-label="Curved asphalt driveway between garden beds"></div>
<div class="abs gallery-item" style="left:870px;background:linear-gradient(90deg,#b79d7c 0%,#c8ad88 45%,#2b2b2b 70%,#d9dcdc 100%)" role="img" aria-label="Narrow sealed path beside a timber fence"></div>

<!-- call to action -->
<div class="abs cta">
  <svg class="abs" style="left:0;top:0" width="1003" height="136" viewBox="0 0 1003 136">
    <polygon points="532,0 1003,0 1003,136 456,136" fill="#f5b21b"/>
    <polygon points="518,0 530,0 454,136 442,136" fill="#ffffff"/>
  </svg>
  <div class="abs cta-ask">Any Questions you would like to ask?</div>
  <div class="abs cta-talk">Need to talk to us...</div>
  <div class="abs cta-numbers">Mobile : 027 555 0199<br>PHONE :09 55 50 142</div>
</div>

<footer class="abs site-footer">
  <nav class="abs footer-nav"><span>HOME</span><span>ABOUT</span><span>SERVICES</span><span>PROJECTS</span><span>CONTACT US</span></nav>
  <div class="abs copyright">©2016 . All rights reserved</div>
  <span class="abs social" style="left:907px"></span>
  <span class="abs social" style="left:982px"></span>
  <span class="abs social" style="left:1055px"></span>
</footer>

</body>
</html>
```